Business Card Design Project Lumaro Foundation

Looking for business card options to match our concurrent logo project on sketch forge. We are a international humanitarian aid firm. We work in the non profit sector but operate more closely to a traditional for-profit investment firm. As such we would like equal tones in our branding materials, which includes are business cards.

Stand by for logo...
Updates

logo uploaded.

Target Market(s)

Adults in western speaking countries ages 18-40 that work primarily in the NGO and Business Administrative Career Field.

Industry/Entity Type

Non Profit

Font styles to use
Sans Serif

Requirements
Nice to have
• We would like all contact information on one side.

Company Name/Logo, Individual Name and Position on the other...

```html
<!DOCTYPE html>
<html lang="en">
<head>
<meta charset="utf-8">
<title>Lumaro Foundation — Business Card</title>
<link rel="stylesheet" href="https://fonts.googleapis.com/css2?family=Montserrat:wght@500&family=Open+Sans:wght@400;600&display=swap">
<style>
  :root {
    --page-bg: #e9e7e4;
    --card-white: #ffffff;
    --card-grey: #ececec;
    --brand-blue: #1d86c8;
    --brand-blue-light: #3a9ad6;
    --brand-blue-dark: #0f6fae;
    --brand-green: #7ab648;
    --ink-grey: #4a4a4c;
    --text-white: #ffffff;
  }
  * { box-sizing: border-box; margin: 0; padding: 0; }
  html, body {
    width: 1200px; height: 1200px; overflow: hidden;
    background: var(--page-bg);
  }
  .canvas {
    position: relative; width: 1200px; height: 1200px;
    display: flex; flex-direction: column; align-items: center;
    justify-content: center; gap: 60px;
  }
  .card {
    position: relative; width: 900px; height: 514px; overflow: hidden;
    background: var(--card-white);
    box-shadow: 0 10px 28px rgba(0,0,0,.18);
  }

  /* Front */
  .card--front .front-top {
    position: absolute; left: 0; top: 0; width: 100%; height: 190px;
    background: linear-gradient(180deg, var(--card-white) 0%, var(--card-grey) 100%);
  }
  .card--front .front-band {
    position: absolute; left: 0; top: 190px; width: 100%; height: 240px;
    background: linear-gradient(110deg, var(--brand-blue-light) 0%, var(--brand-blue) 45%, var(--brand-blue-dark) 100%);
  }
  .card--front .front-base {
    position: absolute; left: 0; bottom: 0; width: 100%; height: 84px;
    background: var(--brand-green);
  }
  .brand {
    position: absolute; display: flex; align-items: center; gap: 22px;
  }
  .brand__mark { background: var(--brand-blue); flex: none; }
  .brand__name {
    font-family: "Montserrat", sans-serif; font-weight: 500;
    color: var(--ink-grey); letter-spacing: .18em; white-space: nowrap;
  }
  .card--front .brand { left: 120px; top: 62px; }
  .card--front .brand__mark { width: 62px; height: 62px; }
  .card--front .brand__name { font-size: 46px; }

  .holder {
    position: absolute; left: 600px; top: 226px;
    font-family: "Open Sans", sans-serif; font-weight: 400;
    color: var(--text-white); font-size: 30px; line-height: 1.45;
  }
  .contact {
    position: absolute; left: 80px; top: 296px; list-style: none;
    font-family: "Open Sans", sans-serif; color: var(--text-white);
    font-size: 24px; line-height: 1.5;
  }
  .contact__item { display: flex; align-items: center; gap: 12px; }
  .contact__icon { width: 20px; height: 20px; flex: none; }
  .social {
    position: absolute; right: 70px; top: 362px; display: flex; gap: 10px;
  }
  .social__box {
    width: 38px; height: 38px; background: var(--brand-blue-dark);
    border: 2px solid var(--text-white);
  }

  /* Back */
  .card--back .back-top {
    position: absolute; left: 0; top: 0; width: 100%; height: 370px;
    background: radial-gradient(ellipse at 50% 40%, var(--card-white) 40%, var(--card-grey) 100%);
  }
  .card--back .back-band {
    position: absolute; left: 0; bottom: 0; width: 100%; height: 144px;
    background: var(--brand-blue);
    display: flex; align-items: center; justify-content: center;
  }
  .card--back .brand { left: 50%; top: 146px; transform: translateX(-50%); }
  .card--back .brand__mark { width: 72px; height: 72px; }
  .card--back .brand__name { font-size: 50px; }
  .web {
    font-family: "Open Sans", sans-serif; font-weight: 400;
    color: var(--text-white); font-size: 34px; letter-spacing: .02em;
  }
</style>
</head>
<body>
<main class="canvas">

  <section class="card card--front" aria-label="Business card front">
    <div class="front-top"></div>
    <div class="front-band"></div>
    <div class="front-base"></div>

    <div class="brand">
      <span class="brand__mark"></span>
      <span class="brand__name">Lumaro Foundation</span>
    </div>

    <div class="holder">
      <p class="holder__name">Name</p>
      <p class="holder__title">Title</p>
    </div>

    <ul class="contact">
      <li class="contact__item">
        <svg class="contact__icon" viewBox="0 0 20 20" aria-hidden="true">
          <path d="M5 2 L8 2 L9 6 L7 7.5 Q9 11.5 12.5 13 L14 11 L18 12 L18 15 Q18 18 15 18 Q3 16 2 5 Q2 2 5 2 Z" fill="var(--text-white)"/>
        </svg>
        <span>mobile</span>
      </li>
      <li class="contact__item">
        <svg class="contact__icon" viewBox="0 0 20 20" aria-hidden="true">
          <rect x="2" y="5" width="16" height="11" fill="var(--text-white)"/>
          <path d="M2 5 L10 11 L18 5" fill="none" stroke="var(--brand-blue)" stroke-width="1.4"/>
        </svg>
        <span>email</span>
      </li>
      <li class="contact__item">
        <svg class="contact__icon" viewBox="0 0 20 20" aria-hidden="true">
          <g fill="none" stroke="var(--text-white)" stroke-width="1.4">
            <circle cx="10" cy="10" r="8"/>
            <ellipse cx="10" cy="10" rx="3.5" ry="8"/>
            <line x1="2" y1="10" x2="18" y2="10"/>
          </g>
        </svg>
        <span>web address</span>
      </li>
    </ul>

    <div class="social" aria-hidden="true">
      <span class="social__box"></span>
      <span class="social__box"></span>
    </div>
  </section>

  <section class="card card--back" aria-label="Business card back">
    <div class="back-top"></div>
    <div class="brand">
      <span class="brand__mark"></span>
      <span class="brand__name">Lumaro Foundation</span>
    </div>
    <div class="back-band">
      <p class="web">www.website</p>
    </div>
  </section>

</main>
</body>
</html>
```